Road Construction Company needs business cards

We would like a new business card designed for our business.

We're a road construction company based in Qld, Australia.

Can the business card please have the following information on it.

Name: Brent Malvoy
Position: General Manager
Phone: 0471 592 304
Email: Brent.malvoy@quendix.com.au
Address: 87 Harrowgate Ave, Pindarra, QLD, 4000
Website: www.quendix.com.au

Visually we'd like the card to be professional and simple.

Attached is our logo.

Our website is www.quendix.com.au

Target Market(s)

Men aged 25-60

Contact Information for Business Card

As listed in project description

Font styles to use
Serif

Requirements
Must have
• Large logo on back of card

```html
<!DOCTYPE html>
<html lang="en">
<head>
<meta charset="utf-8">
<title>Quendix Business Card</title>
<link rel="stylesheet" href="https://fonts.googleapis.com/css2?family=Montserrat:wght@400;600;800&display=swap">
<style>
  :root {
    --brand-blue: #0a58a8;
    --band-blue: #0563b0;
    --ink: #1a1a1a;
    --paper: #ffffff;
    --backdrop: #e6e6e6;
  }
  * { margin: 0; padding: 0; box-sizing: border-box; }
  html, body {
    width: 1109px;
    height: 1200px;
    overflow: hidden;
    background: var(--backdrop);
    font-family: "Montserrat", sans-serif;
  }
  .card {
    position: absolute;
    left: 146px;
    width: 764px;
    height: 436px;
    background: var(--paper);
  }
  .card--front { top: 106px; }
  .card--back { top: 623px; display: flex; align-items: center; justify-content: center; }

  .brand-name {
    font-family: "Montserrat", sans-serif;
    font-weight: 800;
    color: var(--brand-blue);
    line-height: 1;
    letter-spacing: 1px;
  }
  .card--front .brand-name {
    position: absolute;
    top: 50px;
    right: 40px;
    font-size: 60px;
  }
  .card--back .brand-name {
    font-size: 96px;
    letter-spacing: 2px;
    margin-top: 14px;
  }

  .person-name {
    position: absolute;
    left: 35px;
    top: 206px;
    font-size: 36px;
    font-weight: 600;
    color: var(--brand-blue);
    line-height: 1;
  }
  .person-role {
    position: absolute;
    left: 33px;
    top: 258px;
    font-size: 20px;
    font-weight: 400;
    color: var(--ink);
  }
  .divider {
    position: absolute;
    left: 35px;
    top: 300px;
    width: 729px;
    height: 1px;
    background: var(--ink);
  }
  .contact-list {
    position: absolute;
    left: 35px;
    top: 309px;
    list-style: none;
  }
  .contact-list li {
    display: flex;
    align-items: center;
    height: 32px;
    font-size: 20px;
    color: var(--ink);
  }
  .contact-list svg {
    width: 19px;
    height: 19px;
    margin-right: 10px;
    fill: var(--brand-blue);
    flex: none;
  }
  .address {
    position: absolute;
    right: 35px;
    top: 336px;
    text-align: right;
    font-style: normal;
    font-size: 20px;
    line-height: 29px;
    color: var(--ink);
  }
  .edge-band {
    position: absolute;
    left: 0;
    bottom: 0;
    width: 100%;
    height: 13px;
    background: var(--band-blue);
  }
</style>
</head>
<body>
  <section class="card card--front">
    <div class="brand-name">QUENDIX</div>

    <h1 class="person-name">Brent Malvoy</h1>
    <p class="person-role">General Manager</p>
    <div class="divider"></div>

    <ul class="contact-list">
      <li>
        <svg viewBox="0 0 24 24" aria-hidden="true"><path d="M6.6 10.8c1.4 2.8 3.8 5.1 6.6 6.6l2.2-2.2c.3-.3.7-.4 1-.2 1.1.4 2.3.6 3.6.6.6 0 1 .4 1 1V20c0 .6-.4 1-1 1C10.6 21 3 13.4 3 4c0-.6.4-1 1-1h3.5c.6 0 1 .4 1 1 0 1.3.2 2.5.6 3.6.1.3 0 .7-.2 1l-2.3 2.2z"/><path d="M14 2.5a8 8 0 0 1 7.5 7.5h-1.6A6.4 6.4 0 0 0 14 4.1zM14 6a4.5 4.5 0 0 1 4 4h-1.6A3 3 0 0 0 14 7.6z"/></svg>
        0471 592 304
      </li>
      <li>
        <svg viewBox="0 0 24 24" aria-hidden="true"><path d="M2 5h20v14H2zM3.5 6.5v.4l8.5 6.3 8.5-6.3v-.4zM3.5 8.8v8.7h17V8.8L12 15.1z"/></svg>
        Brent.malvoy@quendix.com.au
      </li>
      <li>
        <svg viewBox="0 0 24 24" aria-hidden="true"><path d="M12 2a10 10 0 1 0 0 20 10 10 0 0 0 0-20zm-1 17.9A8 8 0 0 1 4.1 10L9 15v1a2 2 0 0 0 2 2zm6.9-2.5A2 2 0 0 0 16 16h-1v-3a1 1 0 0 0-1-1H8v-2h2a1 1 0 0 0 1-1V7h2a2 2 0 0 0 2-2v-.4a8 8 0 0 1 2.9 12.8z"/></svg>
        www.quendix.com.au
      </li>
    </ul>

    <address class="address">87 Harrowgate Ave,<br>Pindarra, QLD, 4000</address>

    <div class="edge-band"></div>
  </section>

  <section class="card card--back">
    <div class="brand-name">QUENDIX</div>
  </section>
</body>
</html>
```